Bloom Ferry Kite Business cards

Logo, tag line and photo on card
Agent Name
Title
Address
Phone number
Email
Website
Make logo on one side large by rotating  to portrait format.  Keep the background of the logo white.

Contact Information for Business Card
Slogan; Keeping Each Kite Aloft

```html
<!DOCTYPE html>
<html lang="en">
<head>
<meta charset="UTF-8">
<title>Bloom Ferry Kite – Business Cards</title>
<link rel="stylesheet" href="https://fonts.googleapis.com/css2?family=Montserrat:ital,wght@0,400;0,500;0,700;0,800;1,400&display=swap">
<style>
  :root {
    --stage: #bb0407;
    --card: #ffffff;
    --navy: #0d2266;
    --red: #c0161c;
    --grey: #6b6b6b;
    --photo-a: #8a8580;
    --photo-b: #3b3835;
  }
  * { margin: 0; padding: 0; box-sizing: border-box; }
  html, body {
    width: 1200px; height: 1145px; overflow: hidden;
    background: var(--stage);
    font-family: "Montserrat", sans-serif;
  }
  .canvas { position: relative; width: 1200px; height: 1145px; }
  .card {
    position: absolute; top: 396px;
    width: 543px; height: 352px;
    background: var(--card);
    border-radius: 34px;
    box-shadow: 0 6px 18px rgba(0,0,0,.25);
  }
  .card--front { left: 35px; }
  .card--back { left: 607px; }

  .agent-photo {
    position: absolute; left: 27px; top: 107px;
    width: 114px; height: 140px;
    border: 3px solid var(--red); border-radius: 9px;
    background: linear-gradient(160deg, var(--photo-a), var(--photo-b));
  }
  .agent-name {
    position: absolute; left: 161px; top: 105px;
    font-weight: 700; font-size: 24px; color: var(--navy);
    letter-spacing: .2px;
  }
  .agent-title {
    position: absolute; left: 161px; top: 133px;
    font-style: italic; font-size: 10px; color: var(--grey);
  }
  .contact-list { position: absolute; left: 161px; top: 158px; list-style: none; }
  .contact-list li {
    display: flex; align-items: flex-start; gap: 9px;
    font-size: 11px; color: var(--grey); line-height: 13.5px;
    margin-bottom: 6px;
  }
  .contact-list svg { width: 11px; height: 11px; flex: none; margin-top: 1px; fill: var(--red); }

  .wordmark {
    font-weight: 800; color: var(--navy);
    line-height: .95; letter-spacing: -1px;
  }
  .card--front .wordmark {
    position: absolute; left: 397px; top: 122px;
    width: 120px; font-size: 34px;
  }
  .card--back .wordmark {
    position: absolute; left: 0; right: 0; top: 92px;
    text-align: center; font-size: 46px;
  }
  .tagline {
    position: absolute; left: 0; right: 0; top: 255px;
    text-align: center; font-weight: 500; font-size: 13px;
    color: var(--grey); letter-spacing: .6px; text-transform: uppercase;
  }
</style>
</head>
<body>
<main class="canvas">
  <section class="card card--front">
    <div class="agent-photo" role="img" aria-label="Portrait photo of the agent"></div>
    <h1 class="agent-name">Agent Name</h1>
    <p class="agent-title">Agent title</p>
    <ul class="contact-list">
      <li><svg viewBox="0 0 24 24"><path d="M6.6 10.8a15.1 15.1 0 0 0 6.6 6.6l2.2-2.2c.3-.3.7-.4 1-.2 1.1.4 2.3.6 3.6.6.6 0 1 .4 1 1V20c0 .6-.4 1-1 1A17 17 0 0 1 3 4c0-.6.4-1 1-1h3.5c.6 0 1 .4 1 1 0 1.3.2 2.5.6 3.6.1.3 0 .7-.2 1z"/></svg>+1 (000) 000-0000</li>
      <li><svg viewBox="0 0 24 24"><path d="M12 2a10 10 0 1 0 5 18.7l-1-1.7A8 8 0 1 1 20 12v1.2c0 1-.7 1.8-1.5 1.8S17 14.2 17 13.2V12a5 5 0 1 0-1.4 3.5A3.5 3.5 0 0 0 22 13.2V12A10 10 0 0 0 12 2zm0 13a3 3 0 1 1 0-6 3 3 0 0 1 0 6z"/></svg>name@website.com</li>
      <li><svg viewBox="0 0 24 24"><path d="M12 2a10 10 0 1 0 0 20 10 10 0 0 0 0-20zm6.9 6h-2.9a15.6 15.6 0 0 0-1.4-3.6A8 8 0 0 1 18.9 8zM12 4c.8 1.2 1.5 2.5 1.9 4h-3.8c.4-1.5 1.1-2.8 1.9-4zM4.3 14a8 8 0 0 1 0-4h3.4a16.5 16.5 0 0 0 0 4zm.8 2h2.9c.3 1.3.8 2.5 1.4 3.6A8 8 0 0 1 5.1 16zM8 8H5.1a8 8 0 0 1 4.3-3.6C8.8 5.5 8.3 6.7 8 8zm4 12c-.8-1.2-1.5-2.5-1.9-4h3.8c-.4 1.5-1.1 2.8-1.9 4zm2.3-6H9.7a14.7 14.7 0 0 1 0-4h4.6a14.7 14.7 0 0 1 0 4zm.3 5.6c.6-1.1 1.1-2.3 1.4-3.6h2.9a8 8 0 0 1-4.3 3.6zm1.7-5.6a16.5 16.5 0 0 0 0-4h3.4a8 8 0 0 1 0 4z"/></svg>www.website.com</li>
      <li><svg viewBox="0 0 24 24"><path d="M12 2a7 7 0 0 0-7 7c0 5.2 7 13 7 13s7-7.8 7-13a7 7 0 0 0-7-7zm0 9.5a2.5 2.5 0 1 1 0-5 2.5 2.5 0 0 1 0 5z"/></svg>sample address,<br>123 street, NY</li>
    </ul>
    <p class="wordmark">Bloom<br>Ferry<br>Kite</p>
  </section>

  <section class="card card--back">
    <p class="wordmark">Bloom<br>Ferry<br>Kite</p>
    <p class="tagline">Keeping Each Kite Aloft</p>
  </section>
</main>
</body>
</html>
```